Business Card Design Project

I am seeking a business card for my life coaching career. I specialize in coaching executives and entrepreneurs. Consciousness plays a key role in my practice.
Updates

I would like to see different fonts -I don't like the way the capital J looks. I only want my name once on the card, on the front. I like everything centered on the front, with a white background, grey and green on the front; and the same grey on the back with bullet points next to each quality; centered. I like a subtle shadow of the mountains behind the text on the back of the card. I don't want the mountains on either side to be too big. Thank you.

Target Market(s)

Middle age business owners/executives

Industry/Entity Type

Business

Contact Information for Business Card

The front design is my name and a mountain logo. I want to have my name prominently shown.

Requirements
Must have
• Front of card:
• My name prominent sized font
• Helping clients lead more fulfilling lives;
• Executive Life Coach
• 415-362-4807
• pkrelt4@mailvane.net
• Back of Card:
• Providing Unparalleled support
• Providing a safe place to grow in self-awareness
• 20+ years entrepreneurial experience
• Trust
• Integrity
Nice to have
• Easy to read font; warm colors reflecting a masculine personality.

```html
<!DOCTYPE html>
<html lang="en">
<head>
<meta charset="utf-8">
<title>Miles Hartwell – Business Cards</title>
<link rel="stylesheet" href="https://fonts.googleapis.com/css2?family=Arimo:wght@400;700&family=Lobster&display=swap">
<style>
  :root {
    --backdrop: #e6e2dc;
    --card-white: #f4f4f4;
    --slate: #454545;
    --forest: #5b7a38;
    --ink: #333333;
    --on-slate: #f0f0f0;
  }
  * { box-sizing: border-box; margin: 0; padding: 0; }
  html, body { width: 1200px; height: 807px; overflow: hidden; }
  body {
    background: var(--backdrop);
    font-family: "Arimo", Arial, sans-serif;
    position: relative;
  }
  .card {
    position: absolute;
    top: 243px;
    width: 540px;
    height: 320px;
    background: var(--card-white);
    overflow: hidden;
    box-shadow: 0 6px 18px rgba(0,0,0,0.18);
  }
  .card--back { left: 50px; }
  .card--front { left: 610px; }

  /* Back side */
  .band { position: absolute; left: 0; width: 100%; background: var(--slate); }
  .band--top { top: 0; height: 120px; }
  .band--bottom { bottom: 0; height: 108px; }
  .support-line {
    position: absolute; left: 30px; top: 88px;
    color: var(--on-slate); font-size: 15px;
  }
  .qualities {
    position: absolute; left: 30px; bottom: 26px;
    color: var(--on-slate); font-size: 14px; line-height: 1.35;
    list-style: none;
  }
  .brand {
    position: absolute;
    display: flex; flex-direction: column; align-items: center; gap: 4px;
  }
  .brand__row { display: flex; align-items: center; gap: 10px; }
  .brand__mark { width: 18px; height: 18px; background: var(--forest); }
  .brand__name { color: var(--forest); font-weight: 700; font-size: 26px; }
  .brand__tagline { color: var(--ink); font-size: 10px; }
  .card--back .brand { left: 0; right: 0; top: 138px; }

  /* Front side */
  .front-block { position: absolute; background: var(--slate); }
  .front-block--right { left: 300px; right: 0; top: 112px; height: 72px; }
  .front-block--left { left: 0; top: 208px; width: 48px; height: 70px; }
  .identity {
    position: absolute; right: 40px; top: 28px;
    display: flex; flex-direction: column; align-items: flex-start;
  }
  .identity__name {
    font-family: "Lobster", cursive;
    color: var(--forest); font-size: 34px; line-height: 1;
  }
  .identity__title { color: var(--forest); font-size: 20px; margin-top: 2px; }
  .identity__tagline { color: var(--ink); font-size: 11px; margin-top: 4px; }
  .card--front .brand { left: 62px; top: 214px; align-items: flex-start; }
  .contact {
    position: absolute; right: 40px; top: 214px;
    color: var(--forest); font-size: 19px; line-height: 1.3;
    text-align: left;
  }
</style>
</head>
<body>
  <section class="card card--back" aria-label="Card back">
    <div class="band band--top"></div>
    <p class="support-line">Providing Unparalleled support</p>
    <div class="brand">
      <div class="brand__row">
        <span class="brand__mark"></span>
        <span class="brand__name">Miles Hartwell</span>
      </div>
      <span class="brand__tagline">Helping Clients lead more fulfilling lives</span>
    </div>
    <div class="band band--bottom"></div>
    <ul class="qualities">
      <li>Providing a safe place to grow in self-awareness</li>
      <li>20+ years entrepreneurial Experience Trust&nbsp; Integrity</li>
    </ul>
  </section>

  <section class="card card--front" aria-label="Card front">
    <div class="identity">
      <span class="identity__name">Miles Hartwell</span>
      <span class="identity__title">Executive Life Coach</span>
      <span class="identity__tagline">Helping Clients lead more fulfilling lives</span>
    </div>
    <div class="front-block front-block--right"></div>
    <div class="front-block front-block--left"></div>
    <div class="brand">
      <div class="brand__row">
        <span class="brand__mark"></span>
        <span class="brand__name">Miles Hartwell</span>
      </div>
      <span class="brand__tagline">Helping Clients lead more fulfilling lives</span>
    </div>
    <div class="contact">
      <p>pkrelt4@mailvane.net</p>
      <p>415-362-4807</p>
    </div>
  </section>
</body>
</html>
```